Hack my website! Blue Harbor needs a site

We hack stuff. No joke, that is what we do, but we are the good guys!

We do security consulting, specifically offensive security. The technical term is "Penetration Testing", but you probably know it as "hacking". Companies hire us to break in before the bad guys do. (I have a very cool job :) ).

I need a web site to describe our offerings and connect with clients.

I've included my business card and logo so you can understand what I'm looking for on the website and the color scheme.

Tag line:
Offensive Services from Offensive Minds

Target Market(s)

Medium to large businesses

Industry/Entity Type

Computer Security

Coding

Coded - Design and coding required

Number of Pages Required

2 page

Font styles to use
Sans Serif

Colors

Designer to choose colors to be used in the design.

Requirements
Must have
• Flat, clean, professional look
Nice to have
• Bonus for bootstrap. See the uploaded logo for the current colors. I'd really like this to look decent on a phone too.
Should not have
• 1. Black background
• 2. The business card is to show the colors and theme so far. Please, do NOT just slam that into the middle of the site since it doesn't make sense. It feels odd that I have to say that, but I've received multiple submissions where people have done this.

```html
<!DOCTYPE html>
<html lang="en">
<head>
<meta charset="utf-8">
<title>Blue Harbor — Offensive Security</title>
<link href="https://fonts.googleapis.com/css2?family=Montserrat:wght@400;600;700&family=Open+Sans:wght@400;600;700&display=swap" rel="stylesheet">
<style>
:root{
  --red:#d22027;
  --red-dark:#b3181e;
  --ink:#2b2b2b;
  --muted:#8a8a8a;
  --line:#e4e4e4;
  --paper:#ffffff;
  --soft:#f4f4f4;
  --dark:#3a3b3d;
  --darker:#1f2a36;
}
*{box-sizing:border-box;margin:0;padding:0}
html,body{width:1200px;height:3408px;overflow:hidden}
body{background:var(--paper);color:var(--ink);font-family:"Open Sans",Arial,sans-serif;font-size:13px;line-height:1.7}
h1,h2,h3,h4,.brand,.nav a,.stat-num{font-family:"Montserrat",Arial,sans-serif}
.wrap{width:1040px;margin:0 auto;position:relative}

/* Hero */
.hero{height:540px;position:relative;background:linear-gradient(120deg,#cfd8e2 0%,#e8edf2 40%,#b9c6d3 70%,#9aaabb 100%)}
.hero-art{position:absolute;inset:0}
.topbar{position:absolute;top:0;left:0;right:0;height:52px;background:rgba(255,255,255,.35)}
.topbar .wrap{display:flex;align-items:center;justify-content:space-between;height:52px}
.brand{display:flex;align-items:center;gap:8px;font-weight:700;font-size:16px;letter-spacing:1px;color:var(--red)}
.brand .dot{width:14px;height:14px;background:var(--red)}
.nav{display:flex;gap:0}
.nav a{color:#fff;font-size:10px;font-weight:600;letter-spacing:1px;text-decoration:none;padding:0 18px;line-height:52px;border-left:1px solid rgba(255,255,255,.4)}
.hero-title{position:absolute;top:388px;left:0;right:0;text-align:center;color:#fff;font-family:"Montserrat",sans-serif;font-size:22px;letter-spacing:8px;font-weight:400}
.hero-title::after{content:"";display:block;width:40px;height:2px;background:#fff;margin:14px auto 0}

/* About */
.section-title{text-align:center;font-size:18px;letter-spacing:3px;font-weight:600}
.section-title::after{content:"";display:block;width:30px;height:2px;background:var(--red);margin:10px auto 0}
.about{padding-top:40px}
.about-lead{width:560px;margin:16px auto 0;text-align:center;font-size:11px;color:var(--muted)}
.about-lead b{color:var(--ink)}
.about-grid{display:flex;justify-content:space-between;margin-top:60px}
.intro{width:460px}
.intro h3{font-size:13px;letter-spacing:1px;font-weight:600;margin-bottom:14px}
.intro p{font-size:11px;color:var(--muted);margin-bottom:12px}
.intro .more{font-size:10px;font-weight:700;letter-spacing:1px;color:var(--ink)}
.skills{width:470px;padding-top:6px}
.skill{margin-bottom:18px}
.skill-head{display:flex;justify-content:space-between;font-size:9px;font-weight:700;letter-spacing:.5px;margin-bottom:6px}
.skill-bar{height:3px;background:var(--line)}
.skill-bar span{display:block;height:3px;background:var(--red)}

/* Services */
.services{padding-top:150px}
.service-grid{display:grid;grid-template-columns:repeat(3,1fr);column-gap:50px;row-gap:60px;margin-top:80px}
.service{text-align:center}
.service h4{font-size:11px;font-weight:600;letter-spacing:1px;min-height:34px;margin-bottom:14px}
.service-icon{width:120px;height:120px;margin:0 auto 26px;border-radius:50%;background:var(--red);display:flex;align-items:center;justify-content:center;box-shadow:0 0 0 6px #f6d6d7}
.service p{font-size:11px;color:var(--muted);text-align:left;line-height:1.75}

/* Stats */
.stats{margin-top:80px;height:232px;background:linear-gradient(90deg,#2e2f31,#4a4b4e 50%,#2e2f31)}
.stats .wrap{display:flex;justify-content:space-around;align-items:center;height:232px}
.stat{text-align:center;color:#fff}
.stat-num{font-size:40px;font-weight:400;line-height:1}
.stat-label{font-size:10px;letter-spacing:2px;margin-top:8px;font-weight:600}

/* Blog */
.blog{padding-top:32px}
.blog-head{display:flex;justify-content:space-between;align-items:center}
.blog-head h2{font-size:18px;letter-spacing:2px;font-weight:600}
.blog-head a{font-size:10px;font-weight:700;letter-spacing:1px;color:var(--ink);text-decoration:none}
.blog-grid{display:flex;justify-content:space-between;margin-top:50px}
.post{width:316px}
.post-img{height:140px}
.post-meta{font-size:9px;color:var(--muted);margin-top:14px;letter-spacing:.5px}
.post-meta b{color:var(--red)}
.post h4{font-size:11px;font-weight:700;letter-spacing:.5px;margin-top:4px}

/* Tagline */
.tagline{margin-top:92px;height:222px;background:linear-gradient(135deg,#14202c,#243647 55%,#14202c);display:flex;align-items:center;justify-content:center}
.tagline h2{color:#fff;font-size:20px;letter-spacing:3px;font-weight:700}

/* Footer */
.footer{padding-top:40px;height:366px;background:var(--paper)}
.footer-top{display:flex;justify-content:space-between;align-items:center;padding-bottom:20px;border-bottom:1px solid var(--line)}
.brand.footer-brand{font-size:22px}
.brand.footer-brand .dot{width:20px;height:20px}
.subscribe{display:flex;border:1px solid var(--line);width:260px;height:34px}
.subscribe span{flex:1;font-size:10px;color:var(--muted);padding:0 12px;line-height:32px}
.subscribe i{width:34px;background:var(--red)}
.social{display:flex;gap:12px}
.social i{width:14px;height:14px;border-radius:50%;background:var(--dark);display:block}
.footer-cols{display:flex;margin-top:26px}
.footer-about{width:330px;font-size:11px;color:var(--muted)}
.footer-about .more{display:block;margin-top:12px;font-size:10px;font-weight:700;color:var(--ink);letter-spacing:1px}
.footer-links{width:180px;margin-left:60px;list-style:none}
.footer-links li{font-size:10px;font-weight:700;letter-spacing:.5px;line-height:2}
.footer-contact{margin-left:auto;width:220px;font-size:11px;color:var(--muted)}
.footer-contact div{line-height:2}
.copyright{height:88px;background:var(--soft);text-align:center;font-size:10px;color:var(--muted);line-height:88px}
.copyright b{color:var(--red)}
</style>
</head>
<body>

<header class="hero">
  <div class="hero-art" role="img" aria-label="Photo of a hand touching a glowing network of padlock security icons"></div>
  <div class="topbar">
    <div class="wrap">
      <div class="brand"><span class="dot"></span>BLUE HARBOR</div>
      <nav class="nav">
        <a>HOME</a><a>INTRODUCE</a><a>SERVICES</a><a>INFRASTRUCTURE</a><a>CUSTOMERS</a><a>BLOG</a><a>CONTACT</a>
      </nav>
    </div>
  </div>
  <h1 class="hero-title">WELCOME TO BLUE HARBOR</h1>
</header>

<section class="about wrap">
  <h2 class="section-title">ABOUT US.</h2>
  <p class="about-lead"><b>Red Team Adversary Simulation</b> - A goal-based assessment where we attack you like a real world adversary. This includes external attacks and targeted phishing to demonstrate the real risk to your business.</p>
  <div class="about-grid">
    <div class="intro">
      <h3>INTRODUCE</h3>
      <p>Blue Harbor is a security team that helps organisations find weak points before attackers do. We combine deep technical skill with clear reporting so your people know exactly what to fix and why it matters.</p>
      <p>Every engagement is scoped around your goals, tested by hand and delivered with practical guidance your team can act on.</p>
      <span class="more">MORE ABOUT</span>
    </div>
    <div class="skills">
      <div class="skill"><div class="skill-head"><span>INTERNAL PIVOT ASSESSMENT &amp; POST EXPLOITATION</span><span>90%</span></div><div class="skill-bar"><span style="width:90%"></span></div></div>
      <div class="skill"><div class="skill-head"><span>ADVANCED PRODUCT, HARDWARE &amp; RF TESTING</span><span>80%</span></div><div class="skill-bar"><span style="width:80%"></span></div></div>
      <div class="skill"><div class="skill-head"><span>MOBILE APPLICATION ASSESSMENT</span><span>85%</span></div><div class="skill-bar"><span style="width:85%"></span></div></div>
      <div class="skill"><div class="skill-head"><span>EXTERNAL PENETRATION TESTING</span><span>95%</span></div><div class="skill-bar"><span style="width:95%"></span></div></div>
      <div class="skill"><div class="skill-head"><span>INTERNAL PENETRATION TESTING</span><span>90%</span></div><div class="skill-bar"><span style="width:90%"></span></div></div>
      <div class="skill"><div class="skill-head"><span>WEB APPLICATION PENETRATION TESTING</span><span>95%</span></div><div class="skill-bar"><span style="width:95%"></span></div></div>
    </div>
  </div>
</section>

<section class="services wrap">
  <h2 class="section-title">OUR SERVICES.</h2>
  <div class="service-grid">
    <article class="service">
      <h4>INTERNAL PIVOT ASSESSMENT &amp; POST EXPLOITATION</h4>
      <div class="service-icon"><svg width="56" height="56" viewBox="0 0 56 56" fill="none" stroke="#fff" stroke-width="3"><rect x="8" y="10" width="40" height="36" rx="3"/><rect x="18" y="20" width="20" height="14"/><line x1="28" y1="34" x2="28" y2="40"/></svg></div>
      <p>We start as a low privileged user and attempt to move through the network to gain access to key data or systems. This shows what an attacker could reach after a single workstation is compromised, and how far they could go before anyone noticed the activity.</p>
    </article>
    <article class="service">
      <h4>ADVANCED PRODUCT, HARDWARE &amp; RF TESTING</h4>
      <div class="service-icon"><svg width="56" height="56" viewBox="0 0 56 56" fill="none" stroke="#fff" stroke-width="3"><rect x="10" y="10" width="36" height="36" rx="3"/><circle cx="28" cy="28" r="8"/><line x1="28" y1="14" x2="28" y2="18"/><line x1="28" y1="38" x2="28" y2="42"/><line x1="14" y1="28" x2="18" y2="28"/><line x1="38" y1="28" x2="42" y2="28"/></svg></div>
      <p>This is a highly customised assessment designed for your product and hardware. Depending on the device we test wireless signals, firmware, interfaces and physical controls. We have tested a wide range of products from small sensors to full systems.</p>
    </article>
    <article class="service">
      <h4>MOBILE APPLICATION ASSESSMENT</h4>
      <div class="service-icon"><svg width="56" height="56" viewBox="0 0 56 56" fill="none" stroke="#fff" stroke-width="3"><rect x="14" y="6" width="22" height="40" rx="3"/><line x1="22" y1="40" x2="28" y2="40"/><circle cx="40" cy="36" r="7"/></svg></div>
      <p>We look at your mobile application and its supporting services for flaws in configuration, session handling, storage, authentication and access control. Each issue comes with clear steps your developers can follow to fix it.</p>
    </article>
    <article class="service">
      <h4>EXTERNAL PENETRATION TESTING</h4>
      <div class="service-icon"><svg width="56" height="56" viewBox="0 0 56 56" fill="none" stroke="#fff" stroke-width="3"><rect x="8" y="10" width="40" height="28" rx="2"/><line x1="28" y1="38" x2="28" y2="46"/><line x1="18" y1="46" x2="38" y2="46"/></svg></div>
      <p>This includes examination of the public facing systems where we evaluate your exposure and exploit any issues found. We report on the routes an attacker could take from the internet into your organisation.</p>
    </article>
    <article class="service">
      <h4>INTERNAL PENETRATION TESTING</h4>
      <div class="service-icon"><svg width="56" height="56" viewBox="0 0 56 56" fill="none" stroke="#fff" stroke-width="3"><rect x="8" y="8" width="14" height="12"/><rect x="34" y="8" width="14" height="12"/><rect x="21" y="36" width="14" height="12"/><path d="M15 20v8h26v-8M28 28v8"/></svg></div>
      <p>This includes port scans and vulnerability scans of the internal network. We validate the results and look for issues scanners miss. We then show how those weaknesses connect and what risk they present to your organisation.</p>
    </article>
    <article class="service">
      <h4>WEB APPLICATION PENETRATION TESTING</h4>
      <div class="service-icon"><svg width="56" height="56" viewBox="0 0 56 56" fill="none" stroke="#fff" stroke-width="3"><rect x="8" y="10" width="40" height="34" rx="2"/><line x1="8" y1="18" x2="48" y2="18"/><path d="M20 28l-5 5 5 5M36 28l5 5-5 5"/></svg></div>
      <p>Our team will perform end to end analysis of your web application and the related services. This includes authentication, session handling, input handling and business logic. We test manually so nothing is left to an automated tool alone.</p>
    </article>
  </div>
</section>

<section class="stats">
  <div class="wrap">
    <div class="stat"><div class="stat-num">59</div><div class="stat-label">AWARDS</div></div>
    <div class="stat"><div class="stat-num">1054</div><div class="stat-label">STAFF</div></div>
    <div class="stat"><div class="stat-num">34</div><div class="stat-label">CUSTOMER</div></div>
    <div class="stat"><div class="stat-num">154</div><div class="stat-label">PROJECT</div></div>
  </div>
</section>

<section class="blog wrap">
  <div class="blog-head"><h2>LATEST BLOG.</h2><a>VIEW ALL</a></div>
  <div class="blog-grid">
    <article class="post">
      <div class="post-img" role="img" aria-label="Photo of a screen showing a system protected message" style="background:linear-gradient(135deg,#0e3b6b,#1f7bc2 60%,#6fc3f0)"></div>
      <div class="post-meta">BY <b>JOHN DOE</b> &nbsp;|&nbsp; 26 JUNE 2016</div>
      <h4>SYSTEM PROTECTED</h4>
    </article>
    <article class="post">
      <div class="post-img" role="img" aria-label="Photo of networking cables plugged into a switch" style="background:linear-gradient(135deg,#0a2a55,#2a64b8 55%,#8ab7e8)"></div>
      <div class="post-meta">BY <b>JOHN DOE</b> &nbsp;|&nbsp; 26 JUNE 2016</div>
      <h4>C8-NETWORKING</h4>
    </article>
    <article class="post">
      <div class="post-img" role="img" aria-label="Photo of hands typing on a laptop keyboard" style="background:linear-gradient(135deg,#6b7480,#b3b9c1 55%,#dfe2e6)"></div>
      <div class="post-meta">BY <b>JOHN DOE</b> &nbsp;|&nbsp; 26 JUNE 2016</div>
      <h4>COMPUTER-SCIENCE</h4>
    </article>
  </div>
</section>

<section class="tagline" role="img" aria-label="Dark blue technology photo behind the tagline">
  <h2>OFFENSIVE SOLUTIONS FROM OFFENSIVE MINDS</h2>
</section>

<footer class="footer">
  <div class="wrap">
    <div class="footer-top">
      <div class="brand footer-brand"><span class="dot"></span>BLUE HARBOR</div>
      <div class="subscribe"><span>Enter your email</span><i></i></div>
      <div class="social"><i></i><i></i><i></i><i></i><i></i></div>
    </div>
    <div class="footer-cols">
      <div class="footer-about">Blue Harbor is a focused security team that helps medium and large businesses find and fix weak points. We test like attackers and report like partners, with clear steps to keep you safe.<span class="more">READ MORE</span></div>
      <ul class="footer-links">
        <li>HOME</li><li>INTRODUCE</li><li>SERVICES</li><li>INFRASTRUCTURE</li><li>CUSTOMERS</li>
      </ul>
      <ul class="footer-links" style="margin-left:20px">
        <li>BLOG</li><li>CONTACT US</li><li>VISIT CMS</li><li>ASK ADMIN</li>
      </ul>
      <div class="footer-contact">
        <div>18 Harbor Lane, Portside,<br>NY 10000</div>
        <div>info@blueharbor.example</div>
        <div>+1 555 010 2048</div>
      </div>
    </div>
  </div>
</footer>

<div class="copyright">© 2016 <b>Blue Harbor</b> · Security Consultancy</div>

</body>
</html>
```